Beauty Clinic Treatment Menu (Lumen Nails & Beauty)

Needing a treatment menu designed for a beauty clinic in Kauriwai, New Zealand. Like the colours grey, pink, white.
Elegant, Modern and feminine

Lumen Nails & Beauty
Dana Pirrett
Suite 4, 17 Corbel Street
Kauriwai
0271836042
Dana.lumen@mailbay.example
lumenbeauty.example.nz

Target Market(s)

Females

Industry/Entity Type

Beauty Salon

Font styles to use
Serif

Colors

Designer to choose colors to be used in the design.

Requirements
Must have
• Chatterbook and Snapgrid logo

```html
<!DOCTYPE html>
<html lang="en">
<head>
<meta charset="utf-8">
<title>Lumen Nails &amp; Beauty – Trifold Outside</title>
<link rel="stylesheet" href="https://fonts.googleapis.com/css2?family=Oswald:wght@200;300&display=swap">
<style>
  :root {
    --grey-band: #acacac;
    --blush: #e6c6da;
    --blush-quote: #dfb9d0;
    --ink: #1f1f1f;
    --ink-soft: #4a4a4a;
    --bronze: #8a5a3c;
    --paper: #ffffff;
    --guide-bleed: #e0309a;
    --guide-trim: #3fb4e6;
  }
  html, body { margin: 0; padding: 0; overflow: hidden; background: var(--paper); }
  .sheet {
    position: relative;
    width: 1200px;
    height: 933px;
    overflow: hidden;
    background: var(--paper);
    font-family: "Oswald", "Arial Narrow", sans-serif;
    font-weight: 200;
    color: var(--ink);
  }
  .sheet-art { position: absolute; inset: 0; }
  .abs { position: absolute; margin: 0; white-space: nowrap; }

  .panel-heading { font-weight: 200; font-size: 46px; line-height: 1; letter-spacing: -0.5px; }
  .panel-heading--light { color: var(--paper); font-size: 40px; }
  .cover-title { font-weight: 200; font-size: 44px; line-height: 52px; letter-spacing: -0.4px; }

  .testimonial { position: absolute; left: 79px; margin: 0; }
  .testimonial__quote {
    margin: 0; font-size: 17px; line-height: 21.4px; color: var(--ink-soft);
    white-space: nowrap; position: relative;
  }
  .testimonial__quote::before {
    content: "\201C"; position: absolute; left: -17px; top: -15px;
    font-family: Georgia, "Times New Roman", serif; font-weight: 700;
    font-size: 30px; color: var(--blush-quote);
  }
  .testimonial__close {
    display: inline-block; vertical-align: top;
    font-family: Georgia, "Times New Roman", serif; font-weight: 700;
    font-size: 26px; line-height: 20px; height: 12px; overflow: visible;
    color: var(--blush-quote); margin-left: 3px;
  }
  .testimonial__author {
    margin: 21px 0 0; font-size: 17px; line-height: 21px; color: var(--ink-soft);
  }

  .social { left: 459px; display: flex; align-items: center; gap: 16px; font-size: 32px; line-height: 1; }
  .social__dot { width: 30px; height: 30px; border-radius: 50%; flex: none; }
  .social__dot--chatterbook { background: #3d5a98; }
  .social__dot--snapgrid { background: #e4407a; }

  .contact-details { left: 474px; top: 394px; font-style: normal; font-size: 33px; line-height: 41.8px; letter-spacing: -0.3px; }
  .contact-details span { display: block; }
  .contact-details .contact-details__small { font-size: 28px; letter-spacing: -0.5px; }

  .brand-seal { position: absolute; border: 2px solid var(--bronze); border-radius: 50%;
    display: flex; align-items: center; justify-content: center; color: var(--bronze);
    font-weight: 300; box-sizing: border-box; }
  .brand-seal--cover { left: 882px; top: 209px; width: 206px; height: 206px; font-size: 22px; }
  .brand-seal--back { left: 119px; top: 737px; width: 144px; height: 144px; font-size: 15px; }
</style>
</head>
<body>
<div class="sheet">
  <svg class="sheet-art" width="1200" height="933" viewBox="0 0 1200 933" aria-hidden="true">
    <defs>
      <radialGradient id="nail-photo-tone" cx="45%" cy="55%" r="60%">
        <stop offset="0%" stop-color="#e7b9a5"/>
        <stop offset="55%" stop-color="#d9a592"/>
        <stop offset="100%" stop-color="#f4ece9"/>
      </radialGradient>
    </defs>
    <path class="band-top" fill="var(--grey-band)"
      d="M0 0 H1200 V84 C1120 60 1060 50 990 55 C900 60 840 90 792 113 C720 75 640 38 560 38 C480 38 440 55 401 70 C330 95 260 115 187 115 C110 115 50 95 0 85 Z"/>
    <path class="band-bottom" fill="var(--blush)"
      d="M0 747 C60 720 140 700 220 700 C300 700 350 735 401 758 C480 800 560 868 660 868 C720 868 760 864 792 857 C870 830 930 790 1010 780 C1090 772 1150 780 1200 782 V933 H0 Z"/>
    <circle cx="596" cy="518" r="181" fill="var(--blush)"/>
    <circle cx="981" cy="602" r="159" fill="url(#nail-photo-tone)" stroke="var(--blush)" stroke-width="2"
      role="img" aria-label="Photo of a hand with glossy royal blue almond-shaped gel nails"/>
    <g class="guides" fill="none" stroke-width="0.8">
      <rect x="25" y="25" width="1146" height="879" stroke="var(--guide-trim)"/>
      <line x1="401" y1="0" x2="401" y2="933" stroke="var(--guide-bleed)"/>
      <line x1="792" y1="0" x2="792" y2="933" stroke="var(--guide-bleed)"/>
      <g stroke="var(--guide-bleed)" stroke-dasharray="16 18">
        <line x1="0" y1="12" x2="1200" y2="12"/>
        <line x1="0" y1="919" x2="1200" y2="919"/>
        <line x1="13" y1="0" x2="13" y2="933"/>
        <line x1="1187" y1="0" x2="1187" y2="933"/>
      </g>
    </g>
  </svg>

  <!-- Back panel: testimonials -->
  <h2 class="abs panel-heading panel-heading--light" style="left:44px; top:50px;">Testimonials</h2>

  <blockquote class="testimonial" style="top:132px;">
    <p class="testimonial__quote">I absolutely loved every single second of my<br>facial with Dana.<br>I left the salon feeling so relaxed and my skin<br>smooth and glowing. I can't wait for my next<br>appointment.<span class="testimonial__close">&#8221;</span></p>
    <p class="testimonial__author">Mereana Colby</p>
  </blockquote>

  <blockquote class="testimonial" style="top:319px;">
    <p class="testimonial__quote">Dana is an absolute pleasure and a true<br>professional. I can't stop showing off my<br>nails and walked out of her salon feeling<br>pampered and relaxed. Looking forward to<br>booking in for more.<span class="testimonial__close">&#8221;</span></p>
    <p class="testimonial__author">Hazel Wynter</p>
  </blockquote>

  <blockquote class="testimonial" style="top:534px;">
    <p class="testimonial__quote">Just had my first nail appointment and lash<br>tint. I am so happy!! Service was profes–<br>sional and friendly, salon is lovely and cosy. I<br>will be a regular from now on. So happy to<br>have found Dana.<span class="testimonial__close">&#8221;</span></p>
    <p class="testimonial__author">Aria Lockwood</p>
  </blockquote>

  <div class="brand-seal brand-seal--back">Lumen Nails &amp; Beauty</div>

  <!-- Middle panel: contact -->
  <h2 class="abs panel-heading" style="left:449px; top:104px;">Contact</h2>
  <div class="abs social" style="top:215px;"><span class="social__dot social__dot--chatterbook"></span>Lumen Nails &amp; Beauty</div>
  <div class="abs social" style="top:262px;"><span class="social__dot social__dot--snapgrid"></span>lumennailsbeauty</div>

  <address class="abs contact-details">
    <span>Dana Pirrett</span>
    <span>Suite 4, 17 Corbel Street</span>
    <span>Kauriwai</span>
    <span>0271836042</span>
    <span class="contact-details__small">Dana.lumen@mailbay.example</span>
    <span class="contact-details__small">lumenbeauty.example.nz</span>
  </address>

  <!-- Front cover -->
  <h1 class="abs cover-title" style="left:839px; top:94px;">Lumen Nails &amp; Beauty<br>Dana Pirrett</h1>
  <div class="brand-seal brand-seal--cover">Lumen Nails &amp; Beauty</div>
</div>
</body>
</html>
```